I'm looking for an app for customers to order through

I'm looking for an app for my customers to order products through
Ideally each customer would have a customer number with password
Their profile would come up with a preloaded products they currently order
From there they can select the product they require and volume needed for delivery
I would also like an option for them to go to a full product range if they are looking for Ideas or a product they don't currently use
Once the order is completed a copy of the order is them e-mailed to my distribution facilities and a confirmation sent to the customer by e-mail and/or SMS
Current product list is approx 1000 items
Current customers is 80 with expectations to expand to 200
On average current products ordered by each customer is is between 4-8 items
Ordering units are done by both weight and pieces/units

Target Market(s)

Food service outlets,
Restaurant , Hotels, catering companies, clubs, take away shops, cafes
Retail outlets

Number of Pages Required

1 page

Font styles to use
Sans Serif

Colors
abd037

Requirements
Must have
• Customer log in with Password 4 - 6 digit
• Customer order history
Nice to have
• Area for promotions / specials on a weekly / monthly basis

```html
<!DOCTYPE html>
<html lang="en">
<head>
<meta charset="utf-8">
<title>Freshline ordering app screens</title>
<link href="https://fonts.googleapis.com/css2?family=Roboto:wght@300;400;500&display=swap" rel="stylesheet">
<style>
:root{
  --lime:#abd037;
  --lime-dark:#8fb22a;
  --ink:#161616;
  --black:#1a1a1a;
  --white:#ffffff;
  --grey-text:#8a8a8a;
  --grey-band:#efefef;
  --page:#e6e6e6;
  --red:#e8312f;
  --teal:#2aa39b;
  --line:#cfcfcf;
}
*{box-sizing:border-box;margin:0;padding:0}
html,body{width:1031px;height:1200px;overflow:hidden;background:var(--page);font-family:"Roboto",Helvetica,Arial,sans-serif;color:var(--ink)}
.canvas{position:relative;width:1031px;height:1200px}
.screen{position:absolute;width:326px;height:580px;overflow:hidden;background:var(--white)}
.s-login{left:13px;top:13px;background:var(--lime)}
.s-menu{left:353px;top:13px;background:var(--black)}
.s-profile{left:692px;top:13px}
.s-detail{left:13px;top:606px}
.s-cart{left:353px;top:606px}
.s-thanks{left:692px;top:606px}
.abs{position:absolute}
.mid{transform:translateY(-50%)}
.center-x{left:0;right:0;text-align:center}

/* status bar */
.status{position:absolute;left:0;top:0;width:100%;height:19px;font-size:10px;font-weight:500;display:flex;align-items:center;justify-content:space-between;padding:0 5px;z-index:3}
.status.dark{background:var(--black);color:var(--white)}
.status.clear{color:var(--ink)}
.status .carrier,.status .battery{display:flex;align-items:center;gap:3px;width:100px}
.status .battery{justify-content:flex-end}
.status .time{position:absolute;left:0;right:0;text-align:center;pointer-events:none}

/* login */
.login-photo{position:absolute;left:0;top:0;width:100%;height:529px;background:linear-gradient(160deg,#b6d64a 0%,#a4c934 55%,#96bb2e 100%)}
.brand-disc{position:absolute;left:98px;top:77px;width:130px;height:130px;border-radius:50%;background:var(--white);display:flex;align-items:center;justify-content:center;font-size:22px;font-weight:500;color:var(--lime)}
.field-label{top:270px;font-size:14px;color:var(--ink)}
.field-line{left:54px;width:218px;top:290px;height:1px;background:var(--ink)}
.field-dots{top:308px;font-size:14px;letter-spacing:2px}
.btn-outline{left:107px;top:352px;width:112px;height:38px;border:1.5px solid var(--ink);border-radius:19px;display:flex;align-items:center;justify-content:center;font-size:14px}
.login-foot{left:0;top:529px;width:100%;height:51px;background:var(--black)}
.forgot{left:10px;top:555px;color:var(--lime);font-size:14px}
.btn-signup{left:246px;top:539px;width:69px;height:31px;border-radius:16px;background:var(--lime);color:var(--white);font-size:11px;display:flex;align-items:center;justify-content:center}

/* menu */
.menu-item{left:0;display:flex;align-items:center;height:52px;width:240px;color:var(--white);font-size:14px}
.menu-item svg{margin-left:25px;margin-right:14px}
.menu-item.active{color:var(--lime)}
.menu-item.active::before{content:"";position:absolute;left:0;top:0;width:4px;height:100%;background:var(--lime)}
.peek{left:267px;top:73px;width:59px;height:435px;background:var(--white);border-left:2px solid #333;border-top:2px solid #333}
.peek-head{position:absolute;left:0;top:0;width:100%;height:74px;background:var(--black)}
.peek-name{left:9px;top:59px;color:var(--white);font-size:13px;white-space:nowrap}
.peek-label{left:9px;top:98px;font-size:7.5px;color:var(--grey-text);white-space:nowrap}
.thumb{position:absolute;border-radius:50%}

/* header bar */
.topbar{position:absolute;left:0;top:0;width:100%;height:56px;background:var(--black)}
.topbar-title{top:37px;color:var(--white);font-size:14px;font-weight:500}
.back{left:14px;top:29px}

/* profile */
.profile-head{position:absolute;left:0;top:0;width:100%;height:100px;background:var(--black)}
.profile-name{left:12px;top:81px;color:var(--white);font-size:19px}
.avatar{left:249px;top:71px;width:56px;height:56px;border-radius:50%;border:2px solid var(--white);background:linear-gradient(135deg,#d9d4cc,#6d625a)}
.section-label{left:13px;top:135px;font-size:11px;color:#666;letter-spacing:.3px}
.order-row{position:absolute;left:0;width:100%;height:52px}
.order-row .thumb{left:12px;top:0;width:52px;height:52px}
.order-name{position:absolute;left:78px;top:7px;font-size:17px}
.order-sub{position:absolute;left:78px;top:30px;font-size:11px;color:var(--grey-text)}
.order-price{position:absolute;right:12px;top:13px;font-size:19px;color:var(--red);font-weight:300}

/* detail */
.hero{left:0;top:56px;width:100%;height:184px;background:radial-gradient(ellipse at 55% 55%,#8a4a22 0%,#c98a3a 35%,#3f6d1e 70%,#1b1408 100%)}
.details-label{left:13px;top:274px;font-size:11px;color:#666}
.details-body{left:13px;top:290px;width:302px;font-size:14.5px;line-height:18px}
.qty-band{left:0;top:394px;width:100%;height:78px;background:var(--grey-band)}
.qty-num{left:37px;width:40px;text-align:center;top:404px;font-size:35px;font-weight:300}
.qty-unit{left:37px;width:40px;text-align:center;top:447px;font-size:11px;color:#555;letter-spacing:.4px}
.price-big{left:230px;top:420px;font-size:24px;color:var(--red);font-weight:300}
.btn-fill{height:39px;border-radius:20px;background:var(--lime);display:flex;align-items:center;justify-content:space-between;padding:0 14px 0 13px;font-size:14.5px;color:var(--ink)}
.btn-fill.solo{justify-content:center}

/* cart */
.col-head{top:74px;font-size:11px;color:#666;letter-spacing:.4px}
.cart-row{position:absolute;left:0;width:100%;height:40px}
.cart-row .thumb{left:13px;top:0;width:40px;height:40px}
.cart-name{position:absolute;left:64px;top:11px;font-size:14.5px}
.qty-box{position:absolute;left:186px;top:9px;width:23px;height:22px;border:1px solid #555;border-radius:2px;font-size:14px;display:flex;align-items:center;justify-content:center}
.qty-unit-sm{position:absolute;left:213px;top:15px;font-size:11px;color:var(--grey-text)}
.cart-price{position:absolute;right:12px;top:11px;font-size:14.5px}
.divider{left:13px;top:294px;width:301px;height:1px;background:var(--line)}
.subtotal{left:13px;top:318px;font-size:14.5px}
.subtotal-price{right:12px;top:314px;font-size:19px;color:var(--red)}

/* thanks */
.thanks-title{top:272px;font-size:18px}
.thanks-line{font-size:13px;line-height:20px}
.email{color:var(--teal);text-decoration:underline}
</style>
</head>
<body>
<div class="canvas">

  <!-- Sign in -->
  <section class="screen s-login">
    <div class="login-photo" role="img" aria-label="Photo of a man working at a desk in a bright office, tinted lime green"></div>
    <div class="status clear">
      <span class="carrier">●●●●● iRowan
        <svg width="10" height="8" viewBox="0 0 10 8"><path d="M1 3a6 6 0 0 1 8 0M2.7 4.7a3.5 3.5 0 0 1 4.6 0" stroke="currentColor" fill="none" stroke-width="1.2"/><circle cx="5" cy="6.6" r="1" fill="currentColor"/></svg></span>
      <span class="time">9:41 AM</span>
      <span class="battery">100% <svg width="22" height="9" viewBox="0 0 22 9"><rect x=".5" y=".5" width="19" height="8" rx="1.5" fill="none" stroke="currentColor"/><rect x="2" y="2" width="16" height="5" fill="currentColor"/><rect x="20.3" y="3" width="1.4" height="3" fill="currentColor"/></svg></span>
    </div>
    <div class="brand-disc">Freshline</div>
    <div class="abs center-x field-label mid">email address</div>
    <div class="abs field-line"></div>
    <div class="abs center-x field-dots mid">●●●●</div>
    <div class="abs btn-outline">SIGN IN</div>
    <div class="abs login-foot"></div>
    <div class="abs forgot mid">Forgot Password?</div>
    <div class="abs btn-signup">SIGN UP</div>
  </section>

  <!-- Menu -->
  <section class="screen s-menu">
    <div class="status dark">
      <span class="carrier">●●●●● iRowan
        <svg width="10" height="8" viewBox="0 0 10 8"><path d="M1 3a6 6 0 0 1 8 0M2.7 4.7a3.5 3.5 0 0 1 4.6 0" stroke="currentColor" fill="none" stroke-width="1.2"/><circle cx="5" cy="6.6" r="1" fill="currentColor"/></svg></span>
      <span class="time">9:41 AM</span>
      <span class="battery">100% <svg width="22" height="9" viewBox="0 0 22 9"><rect x=".5" y=".5" width="19" height="8" rx="1.5" fill="none" stroke="currentColor"/><rect x="2" y="2" width="16" height="5" fill="currentColor"/><rect x="20.3" y="3" width="1.4" height="3" fill="currentColor"/></svg></span>
    </div>
    <div class="abs menu-item" style="top:188px">
      <svg width="22" height="22" viewBox="0 0 22 22" fill="none" stroke="#fff" stroke-width="1.5"><circle cx="9" cy="9" r="7"/><path d="M14 14l6 6"/></svg>Browse Products</div>
    <div class="abs menu-item active" style="top:240px">
      <svg width="22" height="22" viewBox="0 0 22 22" fill="none" stroke="#abd037" stroke-width="1.5"><circle cx="11" cy="7" r="5"/><path d="M2 21c0-5 4-8 9-8s9 3 9 8z"/></svg>Profile</div>
    <div class="abs menu-item" style="top:292px">
      <svg width="22" height="22" viewBox="0 0 22 22" fill="none" stroke="#fff" stroke-width="1.5"><path d="M1 3h3l3 11h11l2-8H6"/><circle cx="9" cy="18.5" r="1.5"/><circle cx="16" cy="18.5" r="1.5"/></svg>Order History</div>
    <div class="abs menu-item" style="top:344px">
      <svg width="22" height="22" viewBox="0 0 22 22" fill="none" stroke="#fff" stroke-width="1.5"><rect x="1" y="4" width="20" height="14"/><path d="M1 4l10 8 10-8"/></svg>Contact Us</div>
    <div class="abs peek">
      <div class="peek-head"></div>
      <svg class="abs" style="left:9px;top:20px" width="17" height="13" viewBox="0 0 17 13" stroke="#abd037" stroke-width="1.5"><path d="M0 1h17M0 6.5h17M0 12h17"/></svg>
      <div class="abs peek-name">Marco D</div>
      <div class="abs peek-label">CURRENT O</div>
      <div class="thumb" role="img" aria-label="Apples" style="left:9px;top:123px;width:40px;height:40px;background:radial-gradient(#f05b4a,#b81a14)"></div>
      <div class="thumb" role="img" aria-label="Lamb shoulder rack" style="left:9px;top:179px;width:40px;height:40px;background:radial-gradient(#e6b4b0,#8b2a2f)"></div>
      <div class="thumb" role="img" aria-label="Hamburger" style="left:9px;top:235px;width:40px;height:40px;background:radial-gradient(#d6782f,#3b1d10)"></div>
      <div class="thumb" role="img" aria-label="Bananas" style="left:9px;top:291px;width:40px;height:40px;background:radial-gradient(#f7df2a,#c49a0c)"></div>
      <div class="thumb" role="img" aria-label="Pork ribs" style="left:9px;top:347px;width:40px;height:40px;background:radial-gradient(#eec1c1,#9a2b34)"></div>
    </div>
  </section>

  <!-- Profile -->
  <section class="screen s-profile">
    <div class="profile-head"></div>
    <div class="status dark">
      <span class="carrier">●●●●● iRowan
        <svg width="10" height="8" viewBox="0 0 10 8"><path d="M1 3a6 6 0 0 1 8 0M2.7 4.7a3.5 3.5 0 0 1 4.6 0" stroke="currentColor" fill="none" stroke-width="1.2"/><circle cx="5" cy="6.6" r="1" fill="currentColor"/></svg></span>
      <span class="time">9:41 AM</span>
      <span class="battery">100% <svg width="22" height="9" viewBox="0 0 22 9"><rect x=".5" y=".5" width="19" height="8" rx="1.5" fill="none" stroke="currentColor"/><rect x="2" y="2" width="16" height="5" fill="currentColor"/><rect x="20.3" y="3" width="1.4" height="3" fill="currentColor"/></svg></span>
    </div>
    <svg class="abs" style="left:12px;top:29px" width="22" height="16" viewBox="0 0 22 16" stroke="#abd037" stroke-width="1.8"><path d="M0 1h22M0 8h22M0 15h22"/></svg>
    <div class="abs profile-name mid">Marco Delaney</div>
    <div class="abs avatar" role="img" aria-label="Customer profile photo"></div>
    <div class="abs section-label mid">CURRENT ORDERS</div>

    <div class="order-row" style="top:164px">
      <div class="thumb" role="img" aria-label="Apples" style="background:radial-gradient(#f05b4a,#b81a14)"></div>
      <div class="order-name">Apple</div><div class="order-sub">1 dozen</div><div class="order-price">$ 2.00</div>
    </div>
    <div class="order-row" style="top:240px">
      <div class="thumb" role="img" aria-label="Lamb shoulder rack" style="background:radial-gradient(#e6b4b0,#8b2a2f)"></div>
      <div class="order-name">Lamb Shoulder Rack</div><div class="order-sub">1 kilogram</div><div class="order-price">$ 9.70</div>
    </div>
    <div class="order-row" style="top:313px">
      <div class="thumb" role="img" aria-label="Hamburger" style="background:radial-gradient(#d6782f,#3b1d10)"></div>
      <div class="order-name">Hamburger</div><div class="order-sub">2 pieces</div><div class="order-price">$ 5.49</div>
    </div>
    <div class="order-row" style="top:388px">
      <div class="thumb" role="img" aria-label="Bananas" style="background:radial-gradient(#f7df2a,#c49a0c)"></div>
      <div class="order-name">Banana</div><div class="order-sub">1 kilogram</div><div class="order-price">$ 3.90</div>
    </div>
    <div class="order-row" style="top:464px">
      <div class="thumb" role="img" aria-label="Pork ribs" style="background:radial-gradient(#eec1c1,#9a2b34)"></div>
      <div class="order-name">Pork Ribs</div><div class="order-sub">3 kilograms</div><div class="order-price">$ 9.50</div>
    </div>
  </section>

  <!-- Product detail -->
  <section class="screen s-detail">
    <div class="topbar"></div>
    <div class="status dark">
      <span class="carrier">●●●●● iRowan
        <svg width="10" height="8" viewBox="0 0 10 8"><path d="M1 3a6 6 0 0 1 8 0M2.7 4.7a3.5 3.5 0 0 1 4.6 0" stroke="currentColor" fill="none" stroke-width="1.2"/><circle cx="5" cy="6.6" r="1" fill="currentColor"/></svg></span>
      <span class="time">9:41 AM</span>
      <span class="battery">100% <svg width="22" height="9" viewBox="0 0 22 9"><rect x=".5" y=".5" width="19" height="8" rx="1.5" fill="none" stroke="currentColor"/><rect x="2" y="2" width="16" height="5" fill="currentColor"/><rect x="20.3" y="3" width="1.4" height="3" fill="currentColor"/></svg></span>
    </div>
    <svg class="abs back" width="22" height="16" viewBox="0 0 22 16" fill="none" stroke="#abd037" stroke-width="1.6"><path d="M8 1L1 7l7 6M1 7h10a9 9 0 0 1 9 8"/></svg>
    <div class="abs center-x topbar-title mid">Hamburger</div>
    <div class="abs hero" role="img" aria-label="Close-up photo of a cheeseburger with lettuce, tomato and onion"></div>
    <div class="abs details-label mid">DETAILS</div>
    <p class="abs details-body">Lorem ipsum dolor sit amet, consectetur adipiscing elit. Vestibulum dolor elit, mattis non quam sed, sodales vestibulum justo. Cras sed accumsan mi, in auctor nisi.</p>
    <div class="abs qty-band"></div>
    <div class="abs qty-num">2</div>
    <div class="abs qty-unit mid">PIECES</div>
    <svg class="abs" style="left:152px;top:408px" width="22" height="56" viewBox="0 0 22 56" stroke="#161616" stroke-width="1.6"><path d="M1 12h20M11 2v20M1 47h20"/></svg>
    <div class="abs price-big">$ 5.49</div>
    <div class="abs btn-fill" style="left:77px;top:507px;width:173px">Add to Cart
      <svg width="22" height="20" viewBox="0 0 22 20" fill="none" stroke="#161616" stroke-width="1.4"><path d="M1 3h3l3 10h11l2-8H6"/><circle cx="9" cy="17" r="1.5"/><circle cx="16" cy="17" r="1.5"/></svg></div>
  </section>

  <!-- Cart -->
  <section class="screen s-cart">
    <div class="topbar"></div>
    <div class="status dark">
      <span class="carrier">●●●●● iRowan
        <svg width="10" height="8" viewBox="0 0 10 8"><path d="M1 3a6 6 0 0 1 8 0M2.7 4.7a3.5 3.5 0 0 1 4.6 0" stroke="currentColor" fill="none" stroke-width="1.2"/><circle cx="5" cy="6.6" r="1" fill="currentColor"/></svg></span>
      <span class="time">9:41 AM</span>
      <span class="battery">100% <svg width="22" height="9" viewBox="0 0 22 9"><rect x=".5" y=".5" width="19" height="8" rx="1.5" fill="none" stroke="currentColor"/><rect x="2" y="2" width="16" height="5" fill="currentColor"/><rect x="20.3" y="3" width="1.4" height="3" fill="currentColor"/></svg></span>
    </div>
    <svg class="abs back" width="22" height="16" viewBox="0 0 22 16" fill="none" stroke="#abd037" stroke-width="1.6"><path d="M8 1L1 7l7 6M1 7h10a9 9 0 0 1 9 8"/></svg>
    <div class="abs center-x topbar-title mid">Cart</div>
    <div class="abs col-head mid" style="left:13px">ITEM</div>
    <div class="abs col-head mid" style="left:173px">QUANTITY</div>
    <div class="abs col-head mid" style="left:270px">PRICE</div>

    <div class="cart-row" style="top:111px">
      <div class="thumb" role="img" aria-label="Apples" style="background:radial-gradient(#f05b4a,#b81a14)"></div>
      <div class="cart-name">Apple</div><div class="qty-box">1</div><div class="qty-unit-sm">doz</div><div class="cart-price">$ 2.00</div>
    </div>
    <div class="cart-row" style="top:177px">
      <div class="thumb" role="img" aria-label="Hamburger" style="background:radial-gradient(#d6782f,#3b1d10)"></div>
      <div class="cart-name">Hamburger</div><div class="qty-box">2</div><div class="qty-unit-sm">pcs</div><div class="cart-price">$ 5.49</div>
    </div>
    <div class="cart-row" style="top:242px">
      <div class="thumb" role="img" aria-label="Bananas" style="background:radial-gradient(#f7df2a,#c49a0c)"></div>
      <div class="cart-name">Banana</div><div class="qty-box">1</div><div class="qty-unit-sm">kg</div><div class="cart-price">$ 3.90</div>
    </div>
    <div class="abs divider"></div>
    <div class="abs subtotal">Sub Total</div>
    <div class="abs subtotal-price">$ 11.39</div>
    <div class="abs btn-fill" style="left:76px;top:507px;width:173px">Check Out
      <svg width="22" height="22" viewBox="0 0 22 22" fill="none" stroke="#161616" stroke-width="1.4"><circle cx="11" cy="11" r="10"/><path d="M6 11l4 4 6-8"/></svg></div>
  </section>

  <!-- Confirmation -->
  <section class="screen s-thanks">
    <div class="status clear">
      <span class="carrier">●●●●● iRowan
        <svg width="10" height="8" viewBox="0 0 10 8"><path d="M1 3a6 6 0 0 1 8 0M2.7 4.7a3.5 3.5 0 0 1 4.6 0" stroke="currentColor" fill="none" stroke-width="1.2"/><circle cx="5" cy="6.6" r="1" fill="currentColor"/></svg></span>
      <span class="time">9:41 AM</span>
      <span class="battery">100% <svg width="22" height="9" viewBox="0 0 22 9"><rect x=".5" y=".5" width="19" height="8" rx="1.5" fill="none" stroke="currentColor"/><rect x="2" y="2" width="16" height="5" fill="currentColor"/><rect x="20.3" y="3" width="1.4" height="3" fill="currentColor"/></svg></span>
    </div>
    <svg class="abs" style="left:71px;top:58px" width="184" height="184" viewBox="0 0 184 184">
      <circle cx="92" cy="92" r="92" fill="#eef5d8"/>
      <circle cx="92" cy="92" r="82" fill="#dcebb0"/>
      <circle cx="92" cy="92" r="72" fill="none" stroke="#abd037" stroke-width="8"/>
      <circle cx="92" cy="92" r="67" fill="#ffffff"/>
    </svg>
    <div class="abs" role="img" aria-label="Illustration of a shopping basket and bags with a tick" style="left:118px;top:111px;width:90px;height:74px;border-radius:10px;background:linear-gradient(90deg,#e8453c 0%,#e8453c 33%,#2c9fd8 33%,#2c9fd8 66%,#3aa57a 66%)"></div>
    <div class="abs center-x thanks-title mid">Thanks, Rowan.</div>
    <div class="abs center-x thanks-line" style="top:293px">We have received your orders.</div>
    <div class="abs center-x thanks-line" style="top:332px">Should you have any queries about your<br>order, please contact us at<br><span class="email">info@freshlinepantry.com</span></div>
    <div class="abs btn-fill solo" style="left:76px;top:507px;width:174px">Okay</div>
  </section>

</div>
</body>
</html>
```